Business Card Design

After a corporate career in the finance sector I am now operating on my own as a consultant. I require a simple design, and want a strong card which is targeted at a conservative audience.

Target Market(s)

highly educated senior management, directors of companies, finance sector

Industry/Entity Type

Conservative

Contact Information for Business Card

Ruth Danver
Consultant
Mobile: 0417 862 450
Email: ruth.danv@mailcove.net

Requirements
Should not have
• I don't want the colours green/yellow/brown

```html
<!DOCTYPE html>
<html lang="en">
<head>
<meta charset="utf-8">
<title>Ruth Danver — Consultant</title>
<link rel="stylesheet" href="https://fonts.googleapis.com/css2?family=Open+Sans:wght@400;600;700&display=swap">
<style>
  :root {
    --backdrop: #e8e6e3;
    --card-stock: #c8c4bf;
    --card-edge: #bdb8b2;
    --ink-strong: #1f1f1f;
    --ink-soft: #4e4e4e;
    --ink-label: #3f3f3f;
  }
  * { box-sizing: border-box; margin: 0; padding: 0; }
  html, body {
    width: 1200px;
    height: 750px;
    overflow: hidden;
    background: var(--backdrop);
  }
  .canvas {
    position: relative;
    width: 1200px;
    height: 750px;
    display: flex;
    align-items: center;
    justify-content: center;
  }
  .business-card {
    position: relative;
    width: 960px;
    height: 582px;
    background: var(--card-stock);
    border: 1px solid var(--card-edge);
    box-shadow: 0 10px 30px rgba(0, 0, 0, 0.12);
    font-family: "Open Sans", Arial, sans-serif;
  }
  .contact-block {
    position: absolute;
    left: 64px;
    bottom: 72px;
  }
  .identity {
    display: flex;
    align-items: baseline;
    color: var(--ink-strong);
  }
  .identity .name {
    font-size: 34px;
    font-weight: 600;
    letter-spacing: 0.2px;
  }
  .identity .divider {
    font-size: 34px;
    font-weight: 400;
    margin: 0 10px;
  }
  .identity .role {
    font-size: 22px;
    font-weight: 400;
  }
  .details {
    margin-top: 6px;
    font-size: 25px;
    color: var(--ink-soft);
    font-weight: 400;
  }
  .details .label {
    font-weight: 700;
    color: var(--ink-label);
  }
  .details .divider {
    margin: 0 8px;
  }
</style>
</head>
<body>
  <main class="canvas">
    <section class="business-card" aria-label="Business card for Ruth Danver, Consultant">
      <div class="contact-block">
        <p class="identity">
          <span class="name">Ruth Danver</span>
          <span class="divider">|</span>
          <span class="role">Consultant</span>
        </p>
        <p class="details">
          <span class="label">Ph :</span> 0417 862 450<span class="divider">|</span><span class="label">Mail :</span> ruth.danv@mailcove.net
        </p>
      </div>
    </section>
  </main>
</body>
</html>
```